Talvon Crest Real estate in need of Logo design

I just started a new real estate brokerage company and need a professional, new logo design that I can incorporate through all forms of marketing and branding. I would like the business card to use both Matte finish and high gloss.

```html
<!DOCTYPE html>
<html lang="en">
<head>
<meta charset="utf-8">
<title>Talvon Crest Real Estate – Business Card</title>
<link href="https://fonts.googleapis.com/css2?family=Montserrat:wght@500;600;700&family=Roboto:wght@400&display=swap" rel="stylesheet">
<style>
  :root {
    --stage: #2a2a2a;
    --card: #0b0b0b;
    --white: #ffffff;
    --blue: #0bb0ea;
    --orange: #f68a22;
    --red: #e3262d;
    --silver: #c9c9c9;
    --silver-dim: #9a9a9a;
  }
  * { box-sizing: border-box; margin: 0; padding: 0; }
  html, body { width: 1200px; height: 1200px; overflow: hidden; }
  body {
    background: radial-gradient(circle at 50% 30%, #3a3a3a 0%, var(--stage) 55%, #1c1c1c 100%);
    font-family: "Montserrat", sans-serif;
    position: relative;
  }
  .card {
    position: absolute;
    left: 180px;
    width: 840px;
    height: 480px;
    background: var(--card);
    overflow: hidden;
    box-shadow: 0 18px 40px rgba(0,0,0,0.55);
  }
  .card-back { top: 90px; }
  .card-front { top: 630px; }

  /* Back side */
  .back-mark {
    position: absolute;
    left: 350px; top: 80px;
    width: 140px; height: 140px;
    border-radius: 50%;
    background: var(--silver);
  }
  .back-name {
    position: absolute;
    top: 248px; left: 0; width: 100%;
    text-align: center;
    font-weight: 600;
    color: var(--silver);
    line-height: 1.15;
  }
  .back-name .name-main { display: block; font-size: 34px; letter-spacing: 1px; }
  .back-name .name-sub { display: block; font-size: 20px; letter-spacing: 2px; }
  .back-web {
    position: absolute;
    top: 360px; left: 0; width: 100%;
    text-align: center;
    font-family: "Roboto", sans-serif;
    font-size: 17px;
    letter-spacing: 1px;
    color: var(--silver-dim);
  }

  /* Front side */
  .front-name {
    position: absolute;
    left: 56px; top: 44px;
    width: 400px;
    font-weight: 600;
    color: var(--white);
    line-height: 1.15;
    text-align: center;
  }
  .front-name .name-main { display: block; font-size: 38px; letter-spacing: 0.5px; }
  .front-name .name-sub { display: block; font-size: 23px; letter-spacing: 2px; }
  .person {
    position: absolute;
    left: 60px; top: 176px;
  }
  .person-name {
    font-weight: 700;
    font-size: 27px;
    color: var(--blue);
    letter-spacing: 1px;
  }
  .person-role {
    font-weight: 500;
    font-size: 19px;
    color: var(--orange);
    letter-spacing: 1px;
    margin-top: 2px;
  }
  .contact-list {
    position: absolute;
    left: 60px; top: 270px;
    list-style: none;
    font-family: "Roboto", sans-serif;
    font-size: 21px;
    color: var(--white);
  }
  .contact-item {
    display: flex;
    align-items: flex-start;
    gap: 14px;
    line-height: 28px;
    margin-bottom: 6px;
  }
  .contact-icon { width: 22px; height: 22px; margin-top: 3px; flex: none; }
  .front-mark {
    position: absolute;
    left: 530px; top: 70px;
    width: 400px; height: 400px;
    border-radius: 50%;
    background: var(--blue);
  }
</style>
</head>
<body>

<section class="card card-back" aria-label="Card back">
  <div class="back-mark"></div>
  <p class="back-name"><span class="name-main">TALVON CREST</span><span class="name-sub">REAL ESTATE</span></p>
  <p class="back-web">www.talvoncrest.com</p>
</section>

<section class="card card-front" aria-label="Card front">
  <p class="front-name"><span class="name-main">TALVON CREST</span><span class="name-sub">REAL ESTATE</span></p>

  <div class="person">
    <p class="person-name">MARCUS DELANEY</p>
    <p class="person-role">REAL ESTATE BROKER</p>
  </div>

  <ul class="contact-list">
    <li class="contact-item">
      <svg class="contact-icon" viewBox="0 0 24 24"><path fill="var(--red)" d="M6.6 10.8a15 15 0 0 0 6.6 6.6l2.2-2.2c.3-.3.7-.4 1-.2 1.1.4 2.3.6 3.6.6.6 0 1 .4 1 1V20c0 .6-.4 1-1 1A17 17 0 0 1 3 4c0-.6.4-1 1-1h3.5c.6 0 1 .4 1 1 0 1.3.2 2.5.6 3.6.1.3 0 .7-.2 1z"/></svg>
      <span>2483-6107-2294</span>
    </li>
    <li class="contact-item">
      <svg class="contact-icon" viewBox="0 0 24 24"><rect x="2" y="5" width="20" height="14" fill="var(--red)"/><path d="M2 5l10 8 10-8" fill="none" stroke="var(--card)" stroke-width="1.6"/></svg>
      <span>info@talvoncrest.com</span>
    </li>
    <li class="contact-item">
      <svg class="contact-icon" viewBox="0 0 24 24" fill="none" stroke="var(--red)" stroke-width="1.6"><circle cx="12" cy="12" r="9.5"/><ellipse cx="12" cy="12" rx="4" ry="9.5"/><path d="M2.5 12h19M4 7h16M4 17h16"/></svg>
      <span>www.talvoncrest.com</span>
    </li>
    <li class="contact-item">
      <svg class="contact-icon" viewBox="0 0 24 24"><path fill="var(--red)" d="M12 2a7 7 0 0 0-7 7c0 5 7 13 7 13s7-8 7-13a7 7 0 0 0-7-7zm0 9.5A2.5 2.5 0 1 1 12 6.5a2.5 2.5 0 0 1 0 5z"/></svg>
      <span>872 Harbor Pine Road<br>Lakemont, Florida 32790</span>
    </li>
  </ul>

  <div class="front-mark"></div>
</section>

</body>
</html>
```